Curry Sauce label design

Old family recipe for curry sauce passed down thru generations. My Dad, Rafe passed the recipe to me and the family now wants to market the sauce. My father has passed away and we want the sauce to be named after him and the label on the jars to have his picture. Sauce name (for now) is "Rafe's Curry Sauce"

We need a label for the sauce jar. We like the styles of "Dorsetts Pick", "Bo Ul Tessa" and "Bright Crate Co" labels. Use those as style references. I have attached images of those labels and also attached my fathers photo. Note that we want the photo styalized like they did with Dorsetts Pick or other styalization i.e. many photo effects software out there (free) that can turn a photo to line drawing, pastel, oil painting look etc...

the label will need a back label space provided with fonts we can use so we can add the ingredients and nutrition info and other info that you typically see on back of jar. We need label to be able to be upsized or down sized and not lose any resolution or clarity so we can apply to both a 12oz and a 16oz jar
Updates

I will be extending the timeline for this project

Need extra days to review

Industry/Entity Type

Food/sauces/curry sauce

Colors
FFC000
F8CF3A
FAE287
FDF2CF
FEFAEE

Requirements
Must have
• Fathers name and image in label

```html
<!DOCTYPE html>
<html lang="en">
<head>
<meta charset="utf-8">
<title>Rafe's Curry Sauce — Front Label</title>
<link rel="stylesheet" href="https://fonts.googleapis.com/css2?family=Abril+Fatface&family=Syncopate:wght@400;700&family=Michroma&display=swap">
<style>
  :root {
    --backdrop: #d4e88f;
    --rust: #b4502a;
    --rust-dark: #9c4122;
    --gold: #ffc000;
    --gold-soft: #f8cf3a;
    --butter: #fae287;
    --cream: #fdf2cf;
    --ivory: #fefaee;
  }
  html, body {
    margin: 0;
    width: 1200px;
    height: 1069px;
    overflow: hidden;
    background: var(--backdrop);
  }
  .label {
    position: absolute;
    left: 238px;
    top: 84px;
    width: 724px;
    height: 900px;
    display: block;
  }
  .label__ground { fill: var(--rust); }
  .label__edge { fill: var(--gold); }
  .label__hairline { stroke: var(--rust-dark); stroke-width: 1; }
  .badge__arc { fill: none; stroke: var(--gold); stroke-width: 1.6; }
  .badge__title {
    font-family: "Syncopate", sans-serif;
    font-weight: 700;
    font-size: 32px;
    letter-spacing: 3px;
    fill: var(--gold-soft);
  }
  .badge__meta {
    font-family: "Michroma", sans-serif;
    font-size: 11px;
    letter-spacing: 1px;
    fill: var(--ivory);
  }
  .badge__weight {
    font-family: "Michroma", sans-serif;
    font-size: 14px;
    letter-spacing: 2px;
    fill: var(--ivory);
  }
  .badge__tagline {
    font-family: "Syncopate", sans-serif;
    font-weight: 700;
    font-size: 14px;
    letter-spacing: 3px;
    fill: var(--ivory);
  }
  .badge__subline {
    font-family: "Michroma", sans-serif;
    font-size: 10px;
    letter-spacing: 1.5px;
    fill: var(--ivory);
  }
  .portrait__frame { fill: none; stroke: var(--ivory); stroke-width: 5; stroke-dasharray: 2.2 2.2; }
  .portrait__ring { fill: none; stroke: var(--gold); stroke-width: 2; }
  .nameplate__band { fill: var(--ivory); }
  .nameplate__rule { stroke: var(--gold); stroke-width: 1.5; }
  .nameplate__name {
    font-family: "Abril Fatface", serif;
    font-size: 92px;
    letter-spacing: 2px;
    fill: var(--rust);
  }
</style>
</head>
<body>
<svg class="label" viewBox="0 0 555 690" xmlns="http://www.w3.org/2000/svg">
  <defs>
    <radialGradient id="portrait-tone" cx="50%" cy="45%" r="60%">
      <stop offset="0%" stop-color="#e9a04a"/>
      <stop offset="100%" stop-color="#b4502a"/>
    </radialGradient>
    <path id="title-arc" d="M 119 255 A 158 158 0 0 1 435 255"/>
    <path id="tagline-arc" d="M 119 440 A 158 158 0 0 0 435 440"/>
    <path id="subline-arc" d="M 97 440 A 180 180 0 0 0 457 440"/>
  </defs>

  <rect class="label__ground" x="0" y="0" width="555" height="690"/>

  <rect class="label__edge" x="0" y="0" width="555" height="8"/>
  <line class="label__hairline" x1="0" y1="12" x2="555" y2="12"/>
  <rect class="label__edge" x="0" y="24" width="555" height="10" opacity="0.85"/>
  <line class="label__hairline" x1="0" y1="38" x2="555" y2="38"/>

  <line class="label__hairline" x1="0" y1="652" x2="555" y2="652"/>
  <rect class="label__edge" x="0" y="656" width="555" height="10" opacity="0.85"/>
  <line class="label__hairline" x1="0" y1="678" x2="555" y2="678"/>
  <rect class="label__edge" x="0" y="682" width="555" height="8"/>

  <!-- upper badge -->
  <path class="badge__arc" d="M 78 275 A 200 200 0 1 1 476 275"/>
  <path class="badge__arc" d="M 142 255 A 135 135 0 0 1 412 255"/>
  <text class="badge__title" text-anchor="middle">
    <textPath href="#title-arc" startOffset="50%">CURRY SAUCE</textPath>
  </text>
  <text class="badge__meta" x="84" y="322" text-anchor="middle">EST.</text>
  <text class="badge__meta" x="470" y="322" text-anchor="middle">2022</text>

  <!-- portrait medallion -->
  <circle class="portrait__ring" cx="277" cy="255" r="108"/>
  <circle class="portrait__frame" cx="277" cy="255" r="100"/>
  <circle cx="277" cy="255" r="94" fill="url(#portrait-tone)" role="img" aria-label="Stylized portrait of Rafe"/>

  <!-- nameplate -->
  <rect class="nameplate__band" x="0" y="364" width="555" height="114"/>
  <line class="nameplate__rule" x1="0" y1="372" x2="555" y2="372"/>
  <line class="nameplate__rule" x1="0" y1="470" x2="555" y2="470"/>
  <text class="nameplate__name" x="277" y="461" text-anchor="middle">RAFE’S</text>

  <!-- lower badge -->
  <path class="badge__arc" d="M 83.4 490 A 200 200 0 0 0 470.6 490"/>
  <path class="badge__arc" d="M 151.6 490 A 135 135 0 0 0 402.4 490"/>
  <text class="badge__weight" x="277" y="532" text-anchor="middle">12 OZ</text>
  <text class="badge__tagline" text-anchor="middle">
    <textPath href="#tagline-arc" startOffset="50%">OLD FAMILY RECIPE</textPath>
  </text>
  <text class="badge__subline" text-anchor="middle">
    <textPath href="#subline-arc" startOffset="50%">PASSED DOWN THRU GENERATIONS</textPath>
  </text>
</svg>
</body>
</html>
```